In Search of a FANTASTIC BUSINESS CARD REFRESH AND REDESIGN

I would like to redesign the current business card for my company.  There is a parent company, Brookfane Care Group, with 2 operating companies - Brookfane Homecare and Brookfane Senior Living.
I will include the current business card design, along with the 3 logos I would like incorporated.  The business card can be two sided.  I'm looking for something clean, professional, and a fresh new look.

Target Market(s)
Hospitals, social workers, insurance agents, family members of seniors
Industry/Entity Type
Healthcare
Contact Information for Business Card
Name, title of person, address, phone number, web address, email address
Look and feel
Each slider illustrates characteristics of the customer's brand and the style your logo design should communicate.

```html
<!DOCTYPE html>
<html lang="en">
<head>
<meta charset="utf-8">
<title>Brookfane Care Group – Business Card</title>
<link href="https://fonts.googleapis.com/css2?family=Poppins:wght@400;500;600&family=Crimson+Text:ital@1&display=swap" rel="stylesheet">
<style>
  :root {
    --backdrop: #b5b5b5;
    --ink: #060606;
    --paper: #ffffff;
    --rose: #f68f8f;
    --teal: #5a9a95;
    --rule: #9a9a9a;
  }
  * { margin: 0; padding: 0; box-sizing: border-box; }
  html, body { width: 1200px; height: 1200px; overflow: hidden; }
  body {
    background: var(--backdrop);
    position: relative;
    font-family: "Poppins", sans-serif;
  }
  .card {
    position: absolute;
    top: 303px;
    width: 370px;
    height: 594px;
    background: var(--paper);
    overflow: hidden;
    box-shadow: 3px 3px 3px rgba(0,0,0,0.55);
  }
  .card--front { left: 200px; }
  .card--back { left: 600px; width: 364px; }

  /* Front */
  .front-hero {
    position: absolute;
    left: 0; top: 0;
    width: 100%; height: 405px;
    background: var(--ink);
    display: flex;
    flex-direction: column;
    align-items: center;
    justify-content: center;
    gap: 26px;
  }
  .front-hero__square {
    width: 72px; height: 72px;
    border-radius: 10px;
    background: var(--paper);
  }
  .front-hero__name {
    color: var(--paper);
    font-weight: 600;
    font-size: 50px;
    line-height: 1.05;
    text-align: center;
  }
  .front-hero__name small {
    display: block;
    font-size: 26px;
    letter-spacing: 6px;
  }
  .sub-brand {
    position: absolute;
    top: 445px;
    width: 160px;
    display: flex;
    flex-direction: column;
    align-items: center;
    gap: 12px;
  }
  .sub-brand--homecare { left: 17px; }
  .sub-brand--living { left: 180px; }
  .sub-brand__mark { width: 48px; height: 50px; border-radius: 8px; }
  .sub-brand__name {
    font-weight: 500;
    font-size: 21px;
    line-height: 1.15;
    text-align: center;
  }
  .sub-brand__name small { display: block; font-size: 15px; letter-spacing: 1px; }
  .sub-brand--homecare .sub-brand__mark { background: var(--rose); }
  .sub-brand--homecare .sub-brand__name { color: var(--rose); }
  .sub-brand--living .sub-brand__mark { background: var(--teal); }
  .sub-brand--living .sub-brand__name { color: var(--teal); }

  /* Back */
  .back-top {
    position: absolute;
    left: 0; top: 0;
    width: 100%; height: 313px;
    display: flex;
    flex-direction: column;
    align-items: center;
  }
  .company-mark {
    margin-top: 43px;
    width: 83px; height: 83px;
    border-radius: 10px;
    background: var(--ink);
  }
  .company-name {
    margin-top: 22px;
    font-weight: 600;
    font-size: 50px;
    line-height: 1;
    color: var(--ink);
    text-align: center;
  }
  .company-name small {
    display: block;
    margin-top: 8px;
    font-size: 21px;
    letter-spacing: 7px;
  }
  .tagline {
    margin-top: 12px;
    font-family: "Crimson Text", serif;
    font-style: italic;
    font-size: 17px;
    line-height: 1.0;
    text-align: center;
    color: var(--ink);
  }
  .back-bottom {
    position: absolute;
    left: 0; top: 315px; bottom: 0;
    width: 100%;
    background: var(--ink);
    border-top: 2px solid var(--paper);
    box-shadow: 0 -2px 0 var(--ink);
    color: var(--paper);
    text-align: center;
  }
  .person__name {
    margin-top: 30px;
    font-weight: 500;
    font-size: 27px;
    line-height: 1.1;
  }
  .person__title { font-size: 16px; line-height: 1.1; }
  .icon-row {
    margin: 16px auto 0;
    width: 190px;
    display: flex;
    align-items: center;
    gap: 4px;
  }
  .icon-row__rule { flex: 1; height: 1px; background: var(--rule); }
  .icon-chip {
    width: 25px; height: 25px;
    border-radius: 3px;
    background: var(--paper);
    display: flex;
    align-items: center;
    justify-content: center;
  }
  .contact-list {
    margin-top: 12px;
    font-size: 17px;
    line-height: 22px;
    list-style: none;
  }
  .divider {
    margin: 10px auto 0;
    width: 200px; height: 1px;
    background: var(--rule);
  }
  .address {
    margin-top: 8px;
    font-style: normal;
    font-size: 17px;
    line-height: 22px;
  }
</style>
</head>
<body>

<section class="card card--front">
  <div class="front-hero">
    <span class="front-hero__square"></span>
    <span class="front-hero__name">Brookfane<small>Care Group</small></span>
  </div>
  <div class="sub-brand sub-brand--homecare">
    <span class="sub-brand__mark"></span>
    <span class="sub-brand__name">Brookfane<small>Homecare</small></span>
  </div>
  <div class="sub-brand sub-brand--living">
    <span class="sub-brand__mark"></span>
    <span class="sub-brand__name">Brookfane<small>Senior Living</small></span>
  </div>
</section>

<section class="card card--back">
  <div class="back-top">
    <span class="company-mark"></span>
    <h1 class="company-name">Brookfane<small>Care Group</small></h1>
    <p class="tagline">Someone you can depend on...<br>Without question.</p>
  </div>
  <div class="back-bottom">
    <h2 class="person__name">Marla Keane</h2>
    <p class="person__title">President, CEO</p>
    <div class="icon-row">
      <span class="icon-row__rule"></span>
      <span class="icon-chip">
        <svg width="16" height="16" viewBox="0 0 16 16" aria-hidden="true">
          <path d="M2 6c0-2 2-3 6-3s6 1 6 3v1h-3V5.5H5V7H2z" fill="#060606"/>
          <rect x="3.5" y="8" width="9" height="5.5" rx="1" fill="#060606"/>
        </svg>
      </span>
      <span class="icon-chip">
        <svg width="16" height="16" viewBox="0 0 16 16" aria-hidden="true">
          <rect x="2" y="4" width="12" height="8.5" fill="none" stroke="#060606" stroke-width="1.3"/>
          <path d="M2 4l6 5 6-5M2 12.5l4.5-4M14 12.5l-4.5-4" fill="none" stroke="#060606" stroke-width="1.1"/>
        </svg>
      </span>
      <span class="icon-chip">
        <svg width="16" height="16" viewBox="0 0 16 16" aria-hidden="true">
          <circle cx="8" cy="8" r="6" fill="#060606"/>
          <path d="M5 5c2 0 2 2 3 2s1 2-1 3M10 4c1 1 2 2 1 4" fill="none" stroke="#fff" stroke-width="1.2"/>
        </svg>
      </span>
      <span class="icon-row__rule"></span>
    </div>
    <ul class="contact-list">
      <li>(808) 555-0142</li>
      <li>Marla@BrookfaneCare.com</li>
      <li>www.BrookfaneCare.com</li>
    </ul>
    <div class="divider"></div>
    <address class="address">480 Kealoha Ave., Suite 210,<br>Honolulu, HI 96815</address>
  </div>
</section>

</body>
</html>
```